HARD MONEY ORIGINATOR RECRUITMENT.
Looking for individuals to help us originate loans for real estate investor financing primarily used to fix up properties and resell.
HARD MONEY ORIGINATORS WANTED
No Licensing Required
Work As Independent Contractor
1% Flat Finders Fee on Each Loan
Referral Compensation for Recruiting New Originators
Immediate Payouts
Programs Offered Nationwide
Marketing Assistance and Support Available
Email mbelton@corvalendgroup.com for more information or call (800) 641-2957 Ext. 24 Corva Lend Group Services, Inc. www.corvalendgroup.com NMLS #731864
Industry/Entity Type
Real Estate
Look and feel

```html
<!DOCTYPE html>
<html lang="en">
<head>
<meta charset="utf-8">
<title>Hard Money Originator Recruitment</title>
<link rel="stylesheet" href="https://fonts.googleapis.com/css2?family=Open+Sans:wdth,wght@75..100,300..800&display=swap">
<style>
  :root {
    --blue: #0d5aa7;
    --panel-blue: #2b7cc1;
    --gold: #b39a45;
    --gold-pale: #d8cf9f;
    --ink: #222;
    --ink-soft: #3a3a3a;
    --white: #fff;
    --icon-blue: #1f8fd8;
    --icon-olive: #a89a3c;
    --icon-green: #7cbd2c;
  }
  * { margin: 0; padding: 0; box-sizing: border-box; }
  html, body { width: 850px; height: 1200px; overflow: hidden; background: var(--white); }
  body { font-family: "Open Sans", Arial, sans-serif; color: var(--ink); }
  .flyer { position: relative; width: 850px; height: 1200px; background: var(--white); overflow: hidden; }
  .abs { position: absolute; }

  .brand { left: 36px; top: 40px; width: 340px; display: flex; align-items: center; gap: 12px; }
  .brand-dot { width: 58px; height: 58px; border-radius: 50%; background: var(--blue); flex: none; }
  .brand-name { font-size: 22px; font-weight: 700; color: var(--blue); line-height: 1.2; }
  .brand-bar { left: 16px; top: 168px; width: 417px; height: 13px; background: var(--blue); }

  .title { left: 381px; top: 26px; width: 460px; text-align: center; }
  .title-main { font-size: 78px; font-weight: 800; font-stretch: 82%; color: var(--blue); line-height: 1; letter-spacing: 1px; }
  .title-sub { font-size: 36px; font-weight: 700; font-stretch: 82%; color: var(--ink-soft); line-height: 1.2; margin-top: 4px; }

  .photo-family { left: 0; top: 179px; width: 440px; height: 385px;
    background: linear-gradient(135deg, #f2eeea 0%, #d8c3b0 40%, #8a5a3f 70%, #efe9e4 100%); }

  .wanted-panel { left: 440px; top: 179px; width: 410px; height: 385px; background: var(--panel-blue); color: var(--white); }
  .wanted-head { position: absolute; left: 22px; top: 10px; font-size: 47px; font-weight: 800; font-stretch: 85%; line-height: 1; }
  .wanted-head span { display: block; margin-bottom: 2px; }
  .wanted-big { position: absolute; left: 20px; top: 108px; font-size: 72px; font-weight: 300; font-stretch: 85%; line-height: 1; }
  .rule { position: absolute; left: 18px; width: 372px; height: 1px; background: rgba(255,255,255,.7); }
  .no-license { position: absolute; left: 22px; top: 202px; font-size: 33px; font-weight: 700; font-stretch: 82%; line-height: 1; }
  .tool { position: absolute; top: 252px; width: 120px; text-align: center; }
  .tool-icon { width: 80px; height: 80px; border-radius: 50%; border: 3px solid var(--white); margin: 0 auto; display: flex; align-items: center; justify-content: center; }
  .tool-label { font-size: 13px; line-height: 1.15; margin-top: 10px; text-transform: uppercase; }
  .tool-divider { position: absolute; top: 262px; width: 1px; height: 110px; background: rgba(255,255,255,.5); }

  .photo-site { left: 400px; top: 564px; width: 450px; height: 636px;
    background: linear-gradient(160deg, #6f6a66 0%, #4b4543 45%, #2f2b29 100%); }
  .inset { left: 398px; width: 252px; height: 164px; border: 5px solid var(--white); box-shadow: 0 3px 8px rgba(0,0,0,.35); }
  .inset-office { top: 578px; background: linear-gradient(135deg, #e9e4dc, #c9bba6 55%, #5f6a74); }
  .inset-builder { top: 762px; background: linear-gradient(135deg, #d8d3cb, #a67a55 50%, #3b4d6a); }
  .inset-measure { top: 946px; background: linear-gradient(135deg, #e5e5e5, #b7aa98 50%, #4d5b48); }

  .quote { left: 20px; top: 576px; width: 380px; font-size: 23px; line-height: 1.4; color: var(--ink); }
  .quote-mark { color: var(--blue); font-size: 38px; font-weight: 700; line-height: 0; vertical-align: -8px; }
  .quote b { font-weight: 700; color: var(--blue); }
  .quote .gold { color: var(--gold); }
  .quote .line2 { display: block; padding-left: 60px; }

  .perks { left: 28px; top: 684px; width: 370px; list-style: none; }
  .perks li { display: flex; gap: 13px; font-size: 17.5px; font-weight: 600; line-height: 1.35; margin-bottom: 13px; }
  .perks svg { flex: none; margin-top: 4px; }

  .info-pill { left: 0; top: 963px; width: 316px; height: 42px; background: var(--blue); color: var(--white);
    border-radius: 0 10px 10px 0; font-size: 23px; font-weight: 600; padding-left: 28px; line-height: 42px; }
  .contact { left: 32px; top: 1014px; width: 400px; }
  .call { font-size: 27px; display: flex; align-items: center; gap: 6px; }
  .ext { font-size: 17px; margin-top: 8px; }
  .email, .web { font-size: 21px; margin-top: 4px; }
  .email b { color: var(--blue); font-weight: 700; }
  .nmls { left: 279px; top: 1160px; font-size: 16px; font-weight: 700; }
  .gold-bar { left: 0; top: 1184px; width: 415px; height: 16px; background: var(--gold-pale); }
</style>
</head>
<body>
<main class="flyer">
  <div class="abs brand"><span class="brand-dot"></span><span class="brand-name">Corva Lend Group Services, Inc.</span></div>
  <div class="abs brand-bar"></div>

  <header class="abs title">
    <h1 class="title-main">HARD MONEY</h1>
    <p class="title-sub">ORIGINATOR RECRUITMENT</p>
  </header>

  <div class="abs photo-family" role="img" aria-label="Photo of a smiling family of four relaxing together"></div>

  <section class="abs wanted-panel">
    <h2 class="wanted-head"><span>HARD MONEY</span><span>ORIGINATORS</span></h2>
    <p class="wanted-big">WANTED</p>
    <div class="rule" style="top:194px"></div>
    <p class="no-license">NO LICENSING REQUIRED</p>
    <div class="rule" style="top:243px"></div>

    <div class="tool" style="left:25px">
      <div class="tool-icon" style="background:var(--icon-blue)">
        <svg width="44" height="40" viewBox="0 0 44 40" fill="none" stroke="#fff" stroke-width="2.5"><path d="M4 20 L22 6 L40 20"/><rect x="9" y="19" width="26" height="18"/><rect x="18" y="26" width="8" height="11"/><circle cx="22" cy="5" r="4"/></svg>
      </div>
      <p class="tool-label">Loan<br>Programs</p>
    </div>
    <div class="tool-divider" style="left:145px"></div>
    <div class="tool" style="left:145px">
      <div class="tool-icon" style="background:var(--icon-olive)">
        <svg width="34" height="42" viewBox="0 0 34 42" fill="none" stroke="#fff" stroke-width="2.5"><rect x="3" y="3" width="28" height="36" rx="2"/><rect x="8" y="8" width="18" height="7"/><path d="M9 21h4M15 21h4M21 21h4M9 27h4M15 27h4M21 27h4M9 33h4M15 33h4M21 33h4"/></svg>
      </div>
      <p class="tool-label">Mortgage<br>Calculator</p>
    </div>
    <div class="tool-divider" style="left:265px"></div>
    <div class="tool" style="left:265px">
      <div class="tool-icon" style="background:var(--icon-green)">
        <svg width="44" height="40" viewBox="0 0 44 40" fill="#fff"><path d="M22 3 L42 20 H36 V38 H8 V20 H2 Z"/><text x="22" y="33" text-anchor="middle" font-size="20" font-weight="700" fill="#7cbd2c" font-family="Open Sans, sans-serif">$</text></svg>
      </div>
      <p class="tool-label">Loan<br>Rates</p>
    </div>
  </section>

  <div class="abs photo-site" role="img" aria-label="Photo of a construction worker in a hard hat on a renovation site"></div>
  <div class="abs inset inset-office" role="img" aria-label="Photo of an agent and a builder reviewing plans in a renovated room"></div>
  <div class="abs inset inset-builder" role="img" aria-label="Photo of a smiling builder in a hard hat carrying lumber"></div>
  <div class="abs inset inset-measure" role="img" aria-label="Photo of a contractor measuring a wall"></div>

  <p class="abs quote"><span class="quote-mark">“</span>You'll Take the <b>First step...</b><span class="line2">We'll <b class="gold">Handle the Rest</b><span class="quote-mark">”</span></span></p>

  <ul class="abs perks">
    <li><svg width="16" height="16" viewBox="0 0 16 16" fill="none" stroke="#0d5aa7" stroke-width="1.6"><rect x="1" y="1" width="14" height="14"/><path d="M4 8 L7 11 L12 4"/></svg>Work As Independent Contractor</li>
    <li><svg width="16" height="16" viewBox="0 0 16 16" fill="none" stroke="#0d5aa7" stroke-width="1.6"><rect x="1" y="1" width="14" height="14"/><path d="M4 8 L7 11 L12 4"/></svg>1% Flat Finders Fee On Each Loan</li>
    <li><svg width="16" height="16" viewBox="0 0 16 16" fill="none" stroke="#0d5aa7" stroke-width="1.6"><rect x="1" y="1" width="14" height="14"/><path d="M4 8 L7 11 L12 4"/></svg>Referral Compensation For<br>Recruiting New Originators</li>
    <li><svg width="16" height="16" viewBox="0 0 16 16" fill="none" stroke="#0d5aa7" stroke-width="1.6"><rect x="1" y="1" width="14" height="14"/><path d="M4 8 L7 11 L12 4"/></svg>Immediate Payouts</li>
    <li><svg width="16" height="16" viewBox="0 0 16 16" fill="none" stroke="#0d5aa7" stroke-width="1.6"><rect x="1" y="1" width="14" height="14"/><path d="M4 8 L7 11 L12 4"/></svg>Programs Offered Nationwide</li>
    <li><svg width="16" height="16" viewBox="0 0 16 16" fill="none" stroke="#0d5aa7" stroke-width="1.6"><rect x="1" y="1" width="14" height="14"/><path d="M4 8 L7 11 L12 4"/></svg>Marketing Assistance And<br>Support Available</li>
  </ul>

  <div class="abs info-pill">For More Information</div>
  <div class="abs contact">
    <p class="call">Call us:<svg width="22" height="22" viewBox="0 0 24 24" fill="#0d5aa7"><path d="M6.6 10.8a15 15 0 0 0 6.6 6.6l2.2-2.2a1 1 0 0 1 1-.25 11.4 11.4 0 0 0 3.6.57 1 1 0 0 1 1 1V20a1 1 0 0 1-1 1A17 17 0 0 1 3 4a1 1 0 0 1 1-1h3.5a1 1 0 0 1 1 1c0 1.25.2 2.45.57 3.57a1 1 0 0 1-.25 1z"/></svg>(800) 641-2957</p>
    <p class="ext">Ext. 24 Corva Lend Group Services, Inc.</p>
    <p class="email"><b>Email</b> mbelton@corvalendgroup.com</p>
    <p class="web">www.corvalendgroup.com</p>
  </div>
  <p class="abs nmls">NMLS #731864</p>
  <div class="abs gold-bar"></div>
</main>
</body>
</html>
```